Business Card Design Project

We have a logo design and are now looking for a business card design. We supply pre-construction services to the Wireless Telecommunication Industry in the development of cell phone tower and other antenna supporting infrastructure e.g. buildings. The types of services include Real Estate Leasing, Zoning & Permitting,Surveying and A&E work. I am looking for a card that includes the logo we have selected along with the full company name. Company colors are Blue and Silver. I want something professional and that "pops". Use your imagination with the four sided star portion of the logo - it can be stretched such that it occupies a large portion of the card or kept simple the way it is. I am interested in seeing the design on a white, silver, navy, black or charcoal background or any other color you think works well with the logo. Apart from the logo that includes LNI we also need to see the full company name on the card - Lanternway Networks, Inc. The design must also show a persons name, title, address, (2) phone numbers, e-mail address and web address www.lni-sample.co

Target Market(s)

Cell phone carriers e.g. Coravent Mobile, QB&R, K-Cellix, Dunmo etc.

Industry/Entity Type

Cell Phone

Requirements
Must have
• Logo and
Lanternway Networks, Inc.

```html
<!DOCTYPE html>
<html lang="en">
<head>
<meta charset="utf-8">
<title>Lanternway Networks, Inc. – Business Card</title>
<link href="https://fonts.googleapis.com/css2?family=Questrial&family=Cormorant+SC:wght@600&display=swap" rel="stylesheet">
<style>
  :root {
    --stage: #e4e5e7;
    --card-dark: #0c0c0d;
    --card-dark-edge: #2a2b2e;
    --card-light: #ffffff;
    --brand-blue: #1f8fdc;
    --brand-blue-deep: #1570b8;
    --silver: #d3d5d8;
    --silver-deep: #b7babf;
    --silver-text: #c4c7cc;
    --ink: #2b2c2e;
    --ink-soft: #4a4c50;
  }
  * { box-sizing: border-box; margin: 0; padding: 0; }
  html, body { width: 1200px; height: 871px; overflow: hidden; }
  body {
    background: var(--stage);
    font-family: "Questrial", sans-serif;
    position: relative;
  }
  .card {
    position: absolute;
    left: 280px;
    width: 640px;
    height: 366px;
    border-radius: 4px;
    overflow: hidden;
    box-shadow: 0 6px 18px rgba(0,0,0,0.18);
  }

  .lockup {
    position: absolute;
    display: flex;
    flex-direction: column;
    align-items: flex-start;
  }
  .brand {
    display: flex;
    align-items: center;
    gap: 16px;
    color: var(--brand-blue);
    font-family: "Questrial", sans-serif;
    letter-spacing: 4px;
    line-height: 1;
  }
  .brand__dot {
    display: block;
    border-radius: 50%;
    background: var(--brand-blue);
  }
  .company-name {
    font-family: "Questrial", sans-serif;
    letter-spacing: 2px;
    text-transform: uppercase;
    white-space: nowrap;
  }

  /* Front */
  .card--front {
    top: 42px;
    background: linear-gradient(160deg, var(--card-dark-edge) 0%, var(--card-dark) 55%);
  }
  .card--front .lockup {
    left: 50%; top: 50%;
    transform: translate(-50%, -50%);
    align-items: center;
  }
  .card--front .brand { font-size: 96px; }
  .card--front .brand__dot { width: 54px; height: 54px; }
  .card--front .company-name {
    margin-top: 18px;
    font-size: 16px;
    color: var(--silver-text);
    letter-spacing: 4px;
  }

  /* Back */
  .card--back {
    top: 458px;
    background: var(--card-light);
  }
  .card--back .lockup { left: 56px; top: 82px; }
  .card--back .brand { font-size: 64px; }
  .card--back .brand__dot { width: 38px; height: 38px; }
  .card--back .company-name {
    margin-top: 14px;
    font-size: 12px;
    color: var(--ink-soft);
  }

  .contact {
    position: absolute;
    left: 330px;
    top: 84px;
    color: var(--ink-soft);
    font-size: 15px;
    line-height: 1.4;
  }
  .contact__name {
    font-family: "Cormorant SC", serif;
    font-weight: 600;
    font-size: 22px;
    color: var(--ink);
    letter-spacing: 1px;
    line-height: 1;
  }
  .contact__title {
    color: var(--brand-blue);
    font-size: 13px;
    font-weight: bold;
    margin-top: 2px;
  }
  .contact__address { margin-top: 26px; }
  .contact__lines { margin-top: 14px; list-style: none; }
  .contact__lines li {
    display: flex;
    align-items: center;
    gap: 18px;
    line-height: 21px;
  }
  .contact__lines svg { width: 14px; height: 14px; flex: none; }
  .contact__web { margin-top: 8px; }

  .base-band {
    position: absolute;
    left: 0; bottom: 0;
    width: 640px; height: 70px;
  }
</style>
</head>
<body>

<section class="card card--front" aria-label="Card front">
  <div class="lockup">
    <div class="brand"><span class="brand__dot"></span>LNI</div>
    <p class="company-name">Lanternway Networks, Inc.</p>
  </div>
</section>

<section class="card card--back" aria-label="Card back">
  <div class="lockup">
    <div class="brand"><span class="brand__dot"></span>LNI</div>
    <p class="company-name">Lanternway Networks, Inc.</p>
  </div>

  <div class="contact">
    <p class="contact__name">Dara Whitlow</p>
    <p class="contact__title">Ceo</p>
    <p class="contact__address">Level 6, 410 Harbour Road<br>NORTH BAYVALE NSW 2099</p>
    <ul class="contact__lines">
      <li>
        <svg viewBox="0 0 14 14" aria-hidden="true"><path d="M1 5c0-2 2-3 6-3s6 1 6 3v1h-3V5H4v1H1z M3 7h8l1 5H2z" fill="var(--brand-blue)"/></svg>
        02 5550 0148
      </li>
      <li>
        <svg viewBox="0 0 14 14" aria-hidden="true"><rect x="3" y="1" width="8" height="4" fill="none" stroke="var(--brand-blue)" stroke-width="1.4"/><rect x="1" y="5" width="12" height="6" rx="1" fill="var(--brand-blue)"/><rect x="3.5" y="9" width="7" height="4" fill="#fff" stroke="var(--brand-blue)"/></svg>
        02 5550 0195
      </li>
      <li>
        <svg viewBox="0 0 14 14" aria-hidden="true"><rect x="1" y="3" width="12" height="8" fill="var(--brand-blue)"/><path d="M1 3l6 5 6-5" fill="none" stroke="#fff" stroke-width="1.2"/></svg>
        dwhitlow@lni-sample.co
      </li>
    </ul>
    <p class="contact__web">www.lni-sample.co</p>
  </div>

  <svg class="base-band" viewBox="0 0 640 70" aria-hidden="true">
    <polygon points="0,30 370,30 420,70 0,70" fill="var(--brand-blue)"/>
    <polygon points="0,30 370,30 375,34 0,34" fill="var(--brand-blue-deep)"/>
    <polygon points="390,30 640,30 640,70 440,70" fill="var(--silver)"/>
    <polygon points="390,30 640,30 640,34 395,34" fill="var(--silver-deep)"/>
  </svg>
</section>

</body>
</html>
```